Business card design needed

Family General Practitioner/ Family Physician.
Logo is the logo of the Imperial Guild of Community Clinicians Oceania
http://pkvtm.lorimar.example/PictureGallery/logos/pages/IGCCO%20logo_jpg.htm

Reason: Just a bit more time to make changes and the weekend for me to look at things closely and to choose. Thanks, Ulan

Thanks for all the submissions. So many of them are really works of art. Not one of them are not good. The ones that I am eliminating are the ones that I think are not suitable for me personally only, and because if I don't, it makes it very difficult to decide as many of you are also sending me slight variations of a card. I have just decided to choose a second place card too. Can't thank you all enough. Good luck, Ulan. P.S - Working today till 10 pm as the card says :-), so probably won't be able to give a feedback till late Saturday night or Sunday morning here in Sydney, Australia. 

Reason: Just added a second place to the budget and realised that Australia is ahead of the rest of the world in the time zone (only :-) - don't want to offend anyone or start a debate!! ) , so Monday deadline will mean it will be a weekend for the rest of the world. Just wanted to give everyone more time to submit their best, especially since I will be picking a second card too. Can't thank everyone enough for the submissions. P.S - Not keen on photos on the card.

Business

Contact Information for Business Card

Dr. Ulan Pereira M.B.B.S., F.I.G.C.C.O
Family General Practitioner
Address, timings, phone and fax number on the back.

Requirements
Must have
• Timings
Mon 7 am - 7 pm
Tues 7 am - 12 pm
Wed 7 am - 10 pm
Thurs 7 am - 12 pm
Fri 7 am - 8 pm
Sat 8 am - 10 pm
Sun - Off

```html
<!DOCTYPE html>
<html lang="en">
<head>
<meta charset="utf-8">
<title>Dr. Ulan Pereira – Business Card</title>
<link rel="stylesheet" href="https://fonts.googleapis.com/css2?family=Cutive&family=Crimson+Pro:wght@700&family=Open+Sans:wght@400&family=Cinzel:wght@400&display=swap">
<style>
  :root {
    --brand-red: #bb1f2b;
    --paper: #ffffff;
    --ink: #333333;
    --ash: #a9a9a9;
    --backdrop: #eeeae4;
  }
  * { margin: 0; padding: 0; box-sizing: border-box; }
  html, body { width: 1200px; height: 417px; overflow: hidden; }
  body { background: var(--backdrop); position: relative; }

  .card { position: absolute; top: 68px; width: 530px; height: 304px; overflow: hidden; }
  .card svg.card-shape { position: absolute; inset: 0; }
  .card-front { left: 57px; background: var(--paper); }
  .card-back { left: 620px; background: var(--brand-red); color: var(--paper); }

  .guild-mark {
    position: absolute; left: 42px; top: 134px;
    display: flex; align-items: center; gap: 8px;
    font-family: "Cutive", serif; font-size: 20px; color: var(--ink);
  }
  .guild-mark .dot { width: 14px; height: 14px; border-radius: 50%; background: var(--brand-red); }

  .doctor-name {
    position: absolute; left: 224px; top: 100px;
    font-family: "Cutive", serif; font-size: 29px; color: var(--ink); white-space: nowrap;
  }
  .credentials {
    position: absolute; left: 225px; top: 144px;
    font-family: "Cutive", serif; font-size: 12px; letter-spacing: 1px; color: var(--ink);
  }
  .specialty {
    position: absolute; left: 221px; top: 193px;
    font-family: "Cutive", serif; font-size: 17px; color: var(--ink); white-space: nowrap;
  }

  .hours-title {
    position: absolute; left: 61px; top: 83px;
    font-family: "Crimson Pro", serif; font-weight: 700; font-size: 19px;
  }
  .hours-table { position: absolute; left: 36px; top: 114px; border-collapse: collapse; }
  .hours-table td { height: 16.3px; line-height: 16.3px; padding: 0; white-space: nowrap; }
  .hours-table .day { width: 81px; font-family: "Crimson Pro", serif; font-weight: 700; font-size: 15px; }
  .hours-table .sep { width: 20px; font-family: "Open Sans", sans-serif; font-size: 12px; }
  .hours-table .time { font-family: "Open Sans", sans-serif; font-size: 12px; }

  .divider { position: absolute; left: 246px; top: 90px; width: 2px; height: 142px; background: var(--paper); }

  .address {
    position: absolute; left: 273px; top: 134px;
    font-family: "Cinzel", serif; font-size: 11.5px; line-height: 18.5px; letter-spacing: 0.3px;
  }
</style>
</head>
<body>
  <section class="card card-front">
    <svg class="card-shape" width="530" height="304" viewBox="0 0 530 304" aria-hidden="true">
      <path d="M0,0 H530 V40 Q290,35 0,0 Z" fill="var(--brand-red)"/>
      <path d="M0,304 V262 Q90,235 530,304 Z" fill="var(--ash)"/>
    </svg>
    <div class="guild-mark"><span class="dot"></span>IGCCO</div>
    <h1 class="doctor-name">Dr. Ulan Pereira</h1>
    <p class="credentials">M.B.B.S., F.I.G.C.C.O</p>
    <p class="specialty">Family General Practitioner</p>
  </section>

  <section class="card card-back">
    <svg class="card-shape" width="530" height="304" viewBox="0 0 530 304" aria-hidden="true">
      <path d="M40,0 H530 V44 Q300,50 40,0 Z" fill="var(--paper)"/>
      <path d="M0,304 V262 Q90,250 470,304 Z" fill="var(--paper)"/>
    </svg>
    <h2 class="hours-title">Working Hours</h2>
    <table class="hours-table">
      <tr><td class="day">Monday</td><td class="sep">:</td><td class="time">7 AM - &nbsp;7 PM</td></tr>
      <tr><td class="day">Tuesday</td><td class="sep">:</td><td class="time">7 AM - 12 PM</td></tr>
      <tr><td class="day">Wednesday</td><td class="sep">:</td><td class="time">7 AM - 10 PM</td></tr>
      <tr><td class="day">Thursday</td><td class="sep">:</td><td class="time">7 AM - 12 PM</td></tr>
      <tr><td class="day">Friday</td><td class="sep">:</td><td class="time">7 AM - &nbsp;8 PM</td></tr>
      <tr><td class="day">Saturday</td><td class="sep">:</td><td class="time">8 AM - 10 PM</td></tr>
      <tr><td class="day">Sunday</td><td class="sep">:</td><td class="time">OFF</td></tr>
    </table>
    <div class="divider"></div>
    <address class="address" style="font-style:normal">
      Upper Level, Lantern Court,<br>
      Harbour Reach Shopping Center<br>
      Willow Ridge, NSW 2099
    </address>
  </section>
</body>
</html>
```